Coatings & Durability 2019 - Call for papers

We need a flyer designed for the first announcement and call for papers for our 2019 conference. Have had an initial "look and feel" design done last year, however we are looking to find a new designer for ongoing work in 2019. There is the potential for year round work with a budget of $10,000 for various design items and collateral. For this "call for papers" we'd like to inject some fun, fresh ideas. Using the colour scheme and circular theme of the initial look and feel, but am happy for this to be modified/heightened. The conference is in Melbourne and we usually try to have a local theme (ie, grape vines this year for Adelaide). The current design/colours are inspired by Tivoli Pier, however I think it would be cool to incorporate our laneway culture, street art, café culture etc. Happy to change the colours, incorporate more colours etc. This is the first thing people will see for K&D 2019, so we want to WOW them with how cool next year is going to be!
Designer to choose colors to be used in the design.

```html
<!DOCTYPE html>
<html lang="en">
<head>
<meta charset="utf-8">
<title>Coatings &amp; Durability 2019 – First Announcement</title>
<link rel="stylesheet" href="https://fonts.googleapis.com/css2?family=Bebas+Neue&family=Oswald:wght@400;500&family=Josefin+Sans:wght@400;600;700&family=Amatic+SC:wght@700&display=swap">
<style>
  :root {
    --stage: #dedede;
    --red: #d93a52;
    --red-deep: #b42a44;
    --plum: #4d2150;
    --title-green: #1d5a31;
    --pink: #e8455c;
    --blue: #1f86c9;
    --sun: #f3e63c;
    --sun-soft: #f7ef8f;
    --grass: #2f7a2a;
    --grass-dark: #1f5a1f;
    --white: #ffffff;
    --link-blue: #2a8fd6;
    --url-yellow: #f5c518;
  }
  * { box-sizing: border-box; margin: 0; padding: 0; }
  html, body { width: 1200px; height: 675px; overflow: hidden; background: var(--stage); }
  .stage { position: relative; width: 1200px; height: 675px; }
  .flyer-frame { position: absolute; left: 374px; top: 18px; width: 452px; height: 640px; overflow: hidden; box-shadow: 0 6px 18px rgba(0,0,0,.25); }
  .flyer {
    position: absolute; left: 0; top: 0; width: 537px; height: 760px;
    transform: scale(0.8421); transform-origin: 0 0;
    background: radial-gradient(circle at 0 0, var(--plum) 0, #8a2a4c 25%, var(--red) 55%, var(--red-deep) 100%);
    overflow: hidden; font-family: "Josefin Sans", sans-serif;
  }
  .shapes { position: absolute; inset: 0; width: 537px; height: 760px; }
  .abs { position: absolute; }
  .presented { left: 35px; width: 390px; top: 16px; text-align: center; font: 700 8px "Josefin Sans", sans-serif; color: var(--link-blue); letter-spacing: .3px; }
  .host { left: 60px; width: 340px; top: 32px; display: flex; align-items: center; justify-content: center; gap: 8px; }
  .host-dot { width: 34px; height: 34px; border-radius: 50%; background: var(--title-green); flex: none; }
  .host-name { font: 700 13px/1.05 "Josefin Sans", sans-serif; color: var(--title-green); text-transform: uppercase; }
  .title { left: 35px; width: 390px; text-align: center; font-family: "Bebas Neue", sans-serif; color: var(--title-green); line-height: 1; }
  .title-top { top: 88px; font-size: 84px; }
  .title-mid { top: 166px; font-size: 76px; color: var(--pink); display: flex; justify-content: center; align-items: center; gap: 4px; }
  .amp { width: 60px; height: 60px; border-radius: 50%; background: var(--pink); color: var(--white); font: 700 52px/60px "Amatic SC", sans-serif; text-align: center; }
  .title-year { top: 238px; font-size: 82px; color: var(--title-green); -webkit-text-stroke: 1px var(--title-green); letter-spacing: 2px; }
  .date { left: 375px; top: 24px; width: 140px; height: 140px; display: flex; flex-direction: column; justify-content: center; align-items: center; color: var(--title-green); font: 700 30px/1 "Amatic SC", sans-serif; }
  .date .month { font-size: 26px; }
  .venue { left: 27px; top: 295px; width: 156px; height: 156px; display: flex; flex-direction: column; align-items: center; justify-content: center; color: var(--white); font: 400 22px/1.05 "Oswald", sans-serif; text-align: center; text-transform: uppercase; }
  .venue svg { margin-bottom: 6px; }
  .callout { left: 245px; width: 262px; top: 392px; text-align: center; color: var(--white); }
  .callout h2 { font: 500 23px/1.15 "Oswald", sans-serif; text-transform: uppercase; }
  .callout h3 { font: 700 12px "Josefin Sans", sans-serif; margin: 10px 0 6px; }
  .callout p { font: 400 7.6px/1.45 "Josefin Sans", sans-serif; margin-bottom: 8px; }
  .info { right: 18px; top: 674px; text-align: right; color: var(--white); font: 400 16px/1.3 "Oswald", sans-serif; text-transform: uppercase; }
  .info .url { color: var(--url-yellow); font-size: 23px; line-height: 1.2; }
  .web-icon { right: 18px; top: 640px; width: 26px; height: 26px; border-radius: 50%; background: var(--white); color: var(--grass-dark); font: 700 7px/26px "Josefin Sans", sans-serif; text-align: center; }
</style>
</head>
<body>
<main class="stage">
  <div class="flyer-frame">
    <article class="flyer">
      <svg class="shapes" viewBox="0 0 537 760" aria-hidden="false">
        <defs>
          <linearGradient id="laneway" x1="0" y1="0" x2="0" y2="1"><stop offset="0" stop-color="#a9a39a"/><stop offset="1" stop-color="#5c5650"/></linearGradient>
          <linearGradient id="city" x1="0" y1="0" x2="0" y2="1"><stop offset="0" stop-color="#5d8fc4"/><stop offset="1" stop-color="#8a7b76"/></linearGradient>
          <linearGradient id="street-art" x1="0" y1="0" x2="1" y2="1"><stop offset="0" stop-color="#c2384c"/><stop offset=".5" stop-color="#4a8fc0"/><stop offset="1" stop-color="#3a3f4a"/></linearGradient>
          <radialGradient id="turf"><stop offset="0" stop-color="var(--grass)"/><stop offset="1" stop-color="var(--grass-dark)"/></radialGradient>
        </defs>
        <!-- guide rings -->
        <circle class="ring" cx="230" cy="130" r="232" fill="none" stroke="#fff" stroke-width="2"/>
        <circle class="ring" cx="120" cy="520" r="150" fill="none" stroke="#fff" stroke-width="2"/>
        <circle class="ring" cx="440" cy="295" r="112" fill="none" stroke="#fff" stroke-width="2"/>
        <!-- street art band -->
        <path role="img" aria-label="Photo of a graffiti-covered laneway with painted bins" d="M0,555 Q190,590 318,760 L0,760 Z" fill="url(#street-art)" stroke="#fff" stroke-width="6"/>
        <!-- register panel -->
        <path d="M318,760 Q370,628 537,598 L537,760 Z" fill="url(#turf)" stroke="#fff" stroke-width="6"/>
        <!-- headline disc -->
        <circle cx="230" cy="130" r="195" fill="#fff"/>
        <!-- date disc -->
        <circle cx="445" cy="94" r="80" fill="var(--sun-soft)" opacity=".8"/>
        <circle cx="445" cy="94" r="68" fill="var(--sun)"/>
        <!-- city photo -->
        <circle role="img" aria-label="Photo of modern city towers beside a red arched footbridge" cx="440" cy="295" r="78" fill="url(#city)" stroke="#fff" stroke-width="6"/>
        <!-- venue disc -->
        <circle cx="105" cy="373" r="92" fill="none" stroke="var(--sun)" stroke-width="2"/>
        <circle cx="105" cy="373" r="78" fill="var(--blue)"/>
        <!-- laneway photo -->
        <circle role="img" aria-label="Photo of a cobbled laneway with people walking" cx="118" cy="520" r="90" fill="url(#laneway)" stroke="#fff" stroke-width="7"/>
      </svg>

      <p class="abs presented">PROUDLY PRESENTED BY</p>
      <div class="abs host"><span class="host-dot"></span><span class="host-name">The Southern<br>Coatings Society Inc.</span></div>

      <h1>
        <span class="abs title title-top">Coatings</span>
        <span class="abs title title-mid"><span class="amp">&amp;</span>Durability</span>
        <span class="abs title title-year">2019</span>
      </h1>

      <div class="abs date"><span>25-28</span><span class="month">November</span><span>2019</span></div>

      <div class="abs venue">
        <svg width="16" height="22" viewBox="0 0 16 22"><path d="M8 0C3.6 0 0 3.5 0 7.9 0 13.8 8 22 8 22s8-8.2 8-14.1C16 3.5 12.4 0 8 0zm0 11a3.2 3.2 0 110-6.4A3.2 3.2 0 018 11z" fill="#fff"/></svg>
        <span>Melbourne,<br>Riverside Towers</span>
      </div>

      <section class="abs callout">
        <h2>First Announcement<br>&amp; Call for Papers</h2>
        <h3>The Destination - ADELAIDE</h3>
        <p>Adelaide is an inspiring and dynamic and cultured city. Stylish and artistic it is large enough to be cosmopolitan yet compact and convenient. Renowned across Australia as the Festival City, Adelaide's appreciation of the arts goes hand in hand with excellent food and fine wines. Situated between the beautiful Adelaide Hills and the long white beaches of the Gulf of St. Vincent, Adelaide with a population of approximately 1.2 million is a picturesque city which is tranquil, convenient and has the energy of a modern city.</p>
        <p>Adelaide is conveniently located within an hour's drive of some of Australia's most famous and beautiful wine producing regions including the Barossa Valley. Other sight-seeing areas famous to the area and well worth a visit include the Flinders Ranges and scenic and peaceful Kangaroo Island.</p>
      </section>

      <div class="abs web-icon">www</div>
      <p class="abs info">For more information<br>and to register go to<br><span class="url">kdconference.org</span></p>
    </article>
  </div>
</main>
</body>
</html>
```